Design Shopify E-Commerce Website for Men's Products

Design a Shopify website for men to sell our men's jewelry, cigar and bar accessories, and other men's products. Design should be hip, with like a rock n' roll, biker, whiskey driker flare. Name of the company is "Outlaw Cupboard" and website will be www.OutlawCupboard.com
Homepage will have navigation bar with three categories: Men's Jewelry, Cigar & Bar Products, Man Cave Swag
I will upload our logo, inspiration type pictures and some of the products that we sell
Theme colors should be mainly dark: black, grey, brown, gold

```html
<!DOCTYPE html>
<html lang="en">
<head>
<meta charset="utf-8">
<title>Outlaw Cupboard</title>
<link href="https://fonts.googleapis.com/css2?family=Poppins:wght@400;500;600;700;800&family=Montserrat:wght@400;500;600&display=swap" rel="stylesheet">
<style>
:root{
  --gold:#d4a62a;
  --gold-dark:#b3871b;
  --gold-light:#e6c25a;
  --black:#000;
  --ink:#111;
  --text:#333;
  --grey:#ececec;
  --cream:#fbf8ef;
  --white:#fff;
}
*{margin:0;padding:0;box-sizing:border-box}
html,body{width:1200px;height:4380px;overflow:hidden}
body{font-family:'Poppins',sans-serif;color:var(--text);background:var(--white);position:relative}
.abs{position:absolute}
.eyebrow{color:var(--gold);font-size:16px;letter-spacing:1.5px;text-transform:uppercase;font-weight:400}
.h2{color:var(--ink);font-weight:700;font-size:33px;letter-spacing:1px;text-transform:uppercase}
.center{text-align:center;left:0;width:1200px}
.btn{display:inline-block;font-family:'Montserrat',sans-serif;font-weight:600;font-size:11px;letter-spacing:.8px;text-transform:uppercase;text-align:center}
.btn-gold{background:var(--gold);color:var(--white)}
.btn-black{background:var(--black);color:var(--white)}
.ph{display:block}

/* header */
.header{top:0;left:0;width:1200px;height:102px;background:var(--white)}
.brand{left:100px;top:36px;display:flex;align-items:center;gap:8px;font-weight:700;font-size:17px;color:var(--ink)}
.brand .dot{width:22px;height:22px;border-radius:50%;background:var(--gold)}
.nav{left:352px;top:46px;display:flex;gap:66px;font-family:'Montserrat',sans-serif;font-size:12px;letter-spacing:1px;color:#333}
.icons{left:978px;top:45px;display:flex;gap:28px}

/* hero */
.hero{top:102px;left:0;width:1200px;height:620px;overflow:hidden}
.hero-bg{width:100%;height:100%;background:radial-gradient(ellipse at 52% 70%,#5a3a1c 0%,#2a180b 30%,#000 62%)}
.hero-title{top:158px;color:var(--white);font-weight:800;font-size:48px;line-height:46px;letter-spacing:1.5px}
.hero-sub{top:258px;color:var(--white);font-size:13px;font-weight:500;line-height:20px}
.hero-btn{top:320px;left:547px;width:127px;height:32px;line-height:32px;background:var(--white);color:var(--ink);font-size:10px}

/* products */
.card{top:836px;width:247px;height:378px;border:1.5px solid var(--gold-light);background:var(--white)}
.card .ph{position:absolute;left:38px;top:40px;width:170px;height:130px;border-radius:6px}
.card h3{position:absolute;top:206px;width:100%;text-align:center;color:var(--gold);font-weight:500;font-size:18px}
.card p{position:absolute;top:236px;width:100%;text-align:center;font-size:10px;line-height:13px;color:#555}
.card .price{position:absolute;top:268px;width:100%;text-align:center;font-weight:600;font-size:16px;color:var(--ink)}
.card .btn{position:absolute;top:302px;left:60px;width:126px;height:33px;line-height:33px}
.arrow{top:990px}

/* about */
.about-bg{top:1394px;left:0;width:1200px;height:547px;background:var(--grey)}
.about-text{left:609px;width:440px}
.body-copy{font-size:14.5px;line-height:19.5px;color:#222}

/* jewelry */
.gold-block{top:1941px;left:889px;width:311px;height:524px;background:linear-gradient(135deg,#d6aa31,#c99b22)}

/* blogs */
.blogs-bg{top:2465px;left:0;width:1200px;height:660px;background:var(--cream)}
.blog{top:2604px;width:325px;height:391px;background:var(--white);border-radius:6px;overflow:hidden}
.blog .ph{width:100%;height:185px}
.blog h3{text-align:center;color:var(--gold);font-weight:500;font-size:21px;margin-top:25px}
.blog p{text-align:center;font-size:14.5px;line-height:21px;color:#333;margin:10px 22px 0}
.blog .btn{position:absolute;left:106px;top:328px;width:112px;height:33px;line-height:33px}

/* testimonials */
.quote{top:3352px;width:435px;height:260px;border:1.5px solid var(--gold-light);border-radius:40px;background:var(--white)}
.quote .badge{position:absolute;left:50px;top:-22px;width:58px;height:58px;border-radius:50%;background:var(--gold)}
.quote .quote-body{position:absolute;left:49px;top:58px;width:368px}
.quote p{font-family:'Montserrat',sans-serif;font-size:12.5px;line-height:24.5px;color:#444}
.quote .author{margin-top:12px;color:var(--gold);font-weight:600;font-size:14px;line-height:18px}

/* footer */
.footer{top:3620px;left:0;width:1200px;height:760px;background:var(--black);overflow:hidden}
.f-col h4{font-family:'Montserrat',sans-serif;font-weight:500;font-size:16px;letter-spacing:1.5px;color:var(--white)}
.f-col h4::after{content:"";display:block;width:26px;height:2px;background:var(--gold);margin-top:8px}
.f-col ul{list-style:none;margin-top:10px}
.f-col li{color:#ddd;font-size:12px;line-height:19px}
.contact-row{display:flex;gap:12px;align-items:flex-start;margin-top:14px;color:#ddd;font-size:12px;line-height:18px}
.c-icon{width:30px;height:30px;border-radius:50%;background:var(--gold);flex:none;display:flex;align-items:center;justify-content:center}
.social{display:flex;gap:8px;margin-top:18px}
.social span{width:30px;height:30px;border-radius:50%;background:var(--gold)}
</style>
</head>
<body>

<!-- header -->
<header class="abs header">
  <div class="abs brand"><span class="dot"></span>Outlaw Cupboard</div>
  <nav class="abs nav"><span>MEN'S JEWELRY</span><span>CIGAR &amp; BAR PRODUCTS</span><span>MAN CAVE SWAG</span></nav>
  <div class="abs icons">
    <svg width="20" height="20" viewBox="0 0 20 20" fill="none" stroke="#d4a62a" stroke-width="1.6"><circle cx="8.5" cy="8.5" r="6"/><path d="M13 13l5 5"/></svg>
    <svg width="22" height="22" viewBox="0 0 22 22" fill="none" stroke="#d4a62a" stroke-width="1.6"><circle cx="11" cy="11" r="9.5"/><circle cx="11" cy="9" r="3.2"/><path d="M5 17.5c1.5-2.6 3.6-3.6 6-3.6s4.5 1 6 3.6"/></svg>
    <svg width="20" height="22" viewBox="0 0 20 22" fill="none" stroke="#d4a62a" stroke-width="1.6"><path d="M3 7h14l-1.2 13H4.2z"/><path d="M6.5 7V5a3.5 3.5 0 017 0v2"/></svg>
  </div>
</header>

<!-- hero -->
<section class="abs hero">
  <div class="hero-bg" role="img" aria-label="Glass of whiskey with cigars and an open cigar box on a dark table"></div>
  <svg class="abs" style="left:0;top:470px" width="1200" height="150" viewBox="0 0 1200 150">
    <path d="M0 150 L0 130 C250 90 420 20 700 10 C900 4 1080 40 1200 80 L1200 150 Z" fill="#b3871b"/>
    <path d="M0 150 L0 140 C260 110 430 45 700 35 C900 28 1070 70 1200 120 L1200 150 Z" fill="#d4a62a"/>
    <path d="M0 150 C280 140 450 70 720 60 C920 55 1080 100 1200 150 Z" fill="#fff"/>
  </svg>
</section>
<h1 class="abs center hero-title">WELCOME TO<br>OUTLAW CUPBOARD</h1>
<p class="abs center hero-sub">Lorem ipsum dolor sit amet, consectetur adipisc-<br>ing elit, sed do eiusmod</p>
<a class="abs btn hero-btn">BUY NOW</a>

<!-- products -->
<p class="abs center eyebrow" style="top:738px">PRODUCTS</p>
<h2 class="abs center h2" style="top:760px">MEN'S PRODUCTS</h2>

<svg class="abs arrow" style="left:42px" width="26" height="46" viewBox="0 0 26 46" fill="none" stroke="#444" stroke-width="2"><path d="M23 2L3 23l20 21"/></svg>
<svg class="abs arrow" style="left:1124px" width="26" height="46" viewBox="0 0 26 46" fill="none" stroke="#444" stroke-width="2"><path d="M3 2l20 21L3 44"/></svg>

<div class="abs card" style="left:97px">
  <div class="ph" role="img" aria-label="Wooden cigar humidor with glass lid" style="background:linear-gradient(160deg,#a43a3a,#5e1b1b)"></div>
  <h3>Cigar</h3><p>Lorem ipsum dolor sit amet,<br>consectetur adipiscing</p><div class="price">$15.87</div><a class="btn btn-gold">BUY NOW</a>
</div>
<div class="abs card" style="left:352px">
  <div class="ph" role="img" aria-label="Octagonal cigar ashtray" style="background:linear-gradient(160deg,#8c3030,#3d1212 60%,#bbb)"></div>
  <h3>Cigar Astray</h3><p>Lorem ipsum dolor sit amet,<br>consectetur adipiscing</p><div class="price">$19.87</div><a class="btn btn-gold">BUY NOW</a>
</div>
<div class="abs card" style="left:607px">
  <div class="ph" role="img" aria-label="Silver cross pendant" style="background:linear-gradient(160deg,#e8e8e8,#888)"></div>
  <h3>Pendant</h3><p>Lorem ipsum dolor sit amet,<br>consectetur adipiscing</p><div class="price">$24.87</div><a class="btn btn-gold">BUY NOW</a>
</div>
<div class="abs card" style="left:860px">
  <div class="ph" role="img" aria-label="Silver signet ring" style="background:linear-gradient(160deg,#eee,#7d7d7d)"></div>
  <h3>Cigar</h3><p>Lorem ipsum dolor sit amet,<br>consectetur adipiscing</p><div class="price">$5.87</div><a class="btn btn-gold">BUY NOW</a>
</div>

<!-- about -->
<div class="abs about-bg"></div>
<svg class="abs" style="left:0;top:1310px" width="1200" height="110" viewBox="0 0 1200 110">
  <path d="M0 110 C300 30 500 10 650 12 C850 15 1050 50 1200 110 L1200 110 Z" fill="#ececec"/>
  <path d="M0 110 C300 22 500 2 650 4 C850 7 1050 42 1200 110 L1200 100 C1050 34 850 -2 650 -4 C500 -6 300 14 0 100 Z" fill="#d4a62a"/>
</svg>
<svg class="abs" style="left:135px;top:1423px" width="434" height="434" viewBox="0 0 434 434" fill="none"><circle cx="217" cy="217" r="215" stroke="#d4a62a" stroke-width="2"/></svg>
<div class="abs ph" role="img" aria-label="Whiskey glass, cigar and silver ring on a wooden table" style="left:152px;top:1438px;width:404px;height:404px;border-radius:50%;background:radial-gradient(circle at 45% 45%,#8a5a2c,#3a2211 55%,#120a04)"></div>
<div class="abs about-text" style="top:1502px">
  <p class="eyebrow">WHO WE ARE</p>
  <h2 class="h2" style="font-size:27px;margin-top:6px">ABOUT OUTLAW CUPBOARD</h2>
  <p class="body-copy" style="margin-top:12px">Lorem ipsum dolor sit amet, consectetur adipiscing elit, sed do eiusmod tempor incididunt ut labore et dolore magna aliqua.</p>
  <p class="body-copy" style="margin-top:4px">Quis ipsum suspendisse ultrices gravida. Risus commodo viverra maecenas accumsan lacus vel facilisis. Quis ipsum suspendisse ultrices gravida. Risus commodo viverra mae-cenas accumsan lacus vel facilisis.</p>
  <a class="btn btn-gold" style="margin-top:16px;width:139px;height:33px;line-height:33px">LEARN MORE</a>
</div>

<!-- jewelry -->
<div class="abs gold-block" role="img" aria-label="Gold textured backdrop"></div>
<div class="abs" style="left:144px;top:2072px;width:440px">
  <p class="eyebrow">PRODUCT</p>
  <h2 class="h2" style="font-size:30px;margin-top:2px">MEN'S JEWELRY</h2>
  <p class="body-copy" style="font-size:13.5px;line-height:20px;margin-top:8px">Lorem ipsum dolor sit amet, consectetur adipiscing elit, sed do eiusmod tempor incididunt ut labore et dolore magna aliqua.</p>
  <p class="body-copy" style="font-size:13.5px;line-height:20px;margin-top:5px">Quis ipsum suspendisse ultrices gravida. Risus commodo viver-ra maecenas accumsan lacus vel facilisis. Quis ipsum sus-pendisse ultrices gravida. Risus commodo viverra maecenas ac-cumsan lacus vel facilisis. Risus commodo viverra maecenas ac-cumsan lacus vel facilisis.</p>
  <a class="btn btn-black" style="margin-top:24px;width:139px;height:34px;line-height:34px">LEARN MORE</a>
</div>
<div class="abs ph" role="img" aria-label="Silver rings, chains and cross pendant on wood" style="left:676px;top:2042px;width:366px;height:359px;background:linear-gradient(135deg,#9a5f26,#6b3d15 50%,#a66b2d)"></div>

<!-- blogs -->
<div class="abs blogs-bg"></div>
<p class="abs center eyebrow" style="top:2515px">BLOGS</p>
<h2 class="abs center h2" style="top:2536px;font-size:31px">FEATURED BLOGS</h2>
<div class="abs blog" style="left:92px">
  <div class="ph" role="img" aria-label="Cigar humidor filled with cigars" style="background:linear-gradient(160deg,#9e3434,#5a1818)"></div>
  <h3>CIGARE</h3><p>Work encompasses more than mere employment—it's a conduit for growth, identity, and achievement.</p><a class="btn btn-black">LEARN MORE</a>
</div>
<div class="abs blog" style="left:437px">
  <div class="ph" role="img" aria-label="Octagonal cigar ashtray" style="background:linear-gradient(160deg,#7a2a2a,#3a1010 55%,#c8c8c8)"></div>
  <h3>CIGARASHTRAY</h3><p>Work encompasses more than mere employment—it's a conduit for growth, identity, and achievement.</p><a class="btn btn-black">LEARN MORE</a>
</div>
<div class="abs blog" style="left:782px">
  <div class="ph" role="img" aria-label="Wooden desktop cigar cutter" style="background:linear-gradient(160deg,#c9a27a,#7a3f1c 50%,#4a2510)"></div>
  <h3>CIGARCUTTER</h3><p>Work encompasses more than mere employment—it's a conduit for growth, identity, and achievement.</p><a class="btn btn-black">LEARN MORE</a>
</div>
<svg class="abs" style="left:0;top:3050px" width="1200" height="130" viewBox="0 0 1200 130">
  <path d="M0 15 C250 110 450 120 600 118 C800 115 1000 80 1200 20 L1200 0 L0 0 Z" fill="#fbf8ef"/>
  <path d="M0 15 C250 110 450 120 600 118 C800 115 1000 80 1200 20 L1200 28 C1000 90 800 126 600 128 C450 130 250 120 0 25 Z" fill="#d4a62a"/>
</svg>

<!-- testimonials -->
<p class="abs center eyebrow" style="top:3236px">REVIEWS</p>
<h2 class="abs center h2" style="top:3256px;font-size:30px">TESTIMONIALS</h2>
<svg class="abs" style="left:104px;top:3466px" width="20" height="36" viewBox="0 0 20 36" fill="none" stroke="#333" stroke-width="3"><path d="M17 2L3 18l14 16"/></svg>
<svg class="abs" style="left:1086px;top:3466px" width="20" height="36" viewBox="0 0 20 36" fill="none" stroke="#333" stroke-width="3"><path d="M3 2l14 16L3 34"/></svg>
<div class="abs quote" style="left:158px">
  <div class="badge"><svg width="58" height="58" viewBox="0 0 58 58" fill="#fff"><path d="M17 36c0-8 3-13 9-16l1 3c-3 2-5 4-5 7h4v8h-9zM31 36c0-8 3-13 9-16l1 3c-3 2-5 4-5 7h4v8h-9z"/></svg></div>
  <div class="quote-body">
    <p>My family and I are so appreciative of all the help you've provided to us and for being so patient and flexible with all we've been through and the changes we've thrown your way last minute. I trust this compa-ny explicitly to always send us the right caregiver</p>
    <div class="author">Author Name</div>
  </div>
</div>
<div class="abs quote" style="left:615px">
  <div class="badge"><svg width="58" height="58" viewBox="0 0 58 58" fill="#fff"><path d="M17 36c0-8 3-13 9-16l1 3c-3 2-5 4-5 7h4v8h-9zM31 36c0-8 3-13 9-16l1 3c-3 2-5 4-5 7h4v8h-9z"/></svg></div>
  <div class="quote-body">
    <p>My 93 year-old mom experiences Sundowing and in-sisted on remaining in her home. Without the live-in care provided by Haven Helpers, I don't know how we could have managed it. The aides were well trained and very professional. I would recommend them highly.</p>
    <div class="author">Author Name</div>
  </div>
</div>

<!-- footer -->
<svg class="abs" style="left:0;top:3600px" width="1200" height="200" viewBox="0 0 1200 200">
  <path d="M0 20 C80 120 250 170 500 175 C800 180 1050 120 1200 60 L1200 200 L0 200 Z" fill="#b3871b"/>
  <path d="M0 60 C100 150 280 185 520 188 C820 190 1060 140 1200 100 L1200 200 L0 200 Z" fill="#d4a62a"/>
  <path d="M0 110 C140 180 320 198 540 198 C830 198 1060 170 1200 145 L1200 200 L0 200 Z" fill="#000"/>
</svg>
<footer class="abs footer" style="top:3795px;height:585px">
  <h3 class="abs" style="left:128px;top:72px;color:#fff;font-weight:700;font-size:19px">SUSCRIBE OUR NEWSLETTER</h3>
  <p class="abs" style="left:128px;top:103px;width:370px;color:#aaa;font-size:13px;line-height:17px">Lorem Ipsum has been the industry's standard dummy text ever since the 1500s, when ans..</p>
  <div class="abs" style="left:531px;top:79px;width:349px;height:42px;border:1px solid #777;color:#ccc;font-size:12px;line-height:40px;padding-left:20px">Email Adddres</div>
  <div class="abs btn" style="left:887px;top:79px;width:176px;height:42px;line-height:42px;background:linear-gradient(90deg,#e0bb4a,#c99b22);color:#fff;font-size:12px">SUSCRIBRE</div>
  <div class="abs" style="left:0;top:174px;width:1200px;height:1px;background:#333"></div>

  <div class="abs" style="left:134px;top:300px;display:flex;align-items:center;gap:10px;color:#fff;font-weight:700;font-size:20px"><span style="width:26px;height:26px;border-radius:50%;background:var(--gold)"></span>Outlaw Cupboard</div>

  <div class="abs f-col" style="left:398px;top:236px">
    <h4>NAVIGATION</h4>
    <ul><li>Home</li><li>About Us</li><li>Products</li><li>Blogs</li><li>Contact Us</li></ul>
  </div>
  <div class="abs f-col" style="left:646px;top:236px">
    <h4>CATEGORY</h4>
    <ul><li>Men's Jewelry</li><li>Cigar &amp; Bar Products</li><li>Man Cave Swag</li></ul>
  </div>
  <div class="abs f-col" style="left:888px;top:236px">
    <h4>CONTACT US</h4>
    <div class="contact-row" style="margin-top:14px">
      <span class="c-icon"><svg width="14" height="14" viewBox="0 0 24 24" fill="#fff"><path d="M6.6 10.8a15.1 15.1 0 006.6 6.6l2.2-2.2c.3-.3.7-.4 1-.2 1.1.4 2.3.6 3.6.6.6 0 1 .4 1 1V20c0 .6-.4 1-1 1A17 17 0 013 4c0-.6.4-1 1-1h3.5c.6 0 1 .4 1 1 0 1.3.2 2.5.6 3.6.1.3 0 .7-.2 1z"/></svg></span>
      <span>Phone number<br>+123 4567890</span>
    </div>
    <div class="contact-row">
      <span class="c-icon"><svg width="14" height="12" viewBox="0 0 24 18" fill="none" stroke="#fff" stroke-width="2"><rect x="1" y="1" width="22" height="16" rx="2"/><path d="M1 2l11 8 11-8"/></svg></span>
      <span>Email us<br>info@outlawcupboard.com</span>
    </div>
    <div class="social"><span></span><span></span><span></span><span></span></div>
  </div>

  <div class="abs" style="left:142px;top:524px;width:1003px;height:1px;background:#333"></div>
  <p class="abs" style="left:148px;top:547px;color:#bbb;font-size:10.5px">© 2023 Outlaw Cupboard. All Rights Reserved</p>
  <p class="abs" style="left:840px;top:547px;color:#bbb;font-size:10.5px;word-spacing:2px">Privacy Policy &nbsp;&nbsp; Terms&amp; Conditions &nbsp;&nbsp; Sitemap</p>
</footer>

</body>
</html>
```